Business Card Design needed for logo design project

Our business needs a business card design. I'm not sure what format files are generally delivered back, but clearly I will need the ability to edit to add colleagues contact details.

Our logo is attached.

Brivomar is a 3D design services company, providing app, serious/educational game, VR and AR websites/applications to corporate clients.

Target Market(s)

Corporate blue-chip clients needing 3D design services

Industry/Entity Type

Business

Font styles to use
Sans Serif

Requirements
Must have
• Templated such that I can add details (name, phone number etc). Needs to include logo from previous project winner - attached.

```html
<!DOCTYPE html>
<html lang="en">
<head>
<meta charset="utf-8">
<title>Brivomar Business Card</title>
<link href="https://fonts.googleapis.com/css2?family=Lato:wght@400;700;900&display=swap" rel="stylesheet">
<style>
  :root {
    --bg: #e4e4e4;
    --paper: #f7f7f7;
    --charcoal: #3d3e40;
    --charcoal-dark: #2c2d2f;
    --ink: #4a4b4d;
    --red: #ef1e35;
    --white: #ffffff;
  }
  * { margin: 0; padding: 0; box-sizing: border-box; }
  html, body { width: 1200px; height: 905px; overflow: hidden; }
  body {
    background: var(--bg);
    font-family: 'Lato', sans-serif;
    display: flex;
    flex-direction: column;
    align-items: center;
    justify-content: center;
    gap: 44px;
  }
  .card {
    width: 660px;
    height: 377px;
    position: relative;
    overflow: hidden;
    background: var(--paper);
    box-shadow: 0 6px 18px rgba(0,0,0,0.18);
  }

  /* Front side */
  .brand {
    position: absolute;
    top: 92px;
    left: 0; right: 0;
    display: flex;
    align-items: center;
    justify-content: center;
    gap: 22px;
  }
  .brand-dot {
    width: 86px; height: 86px;
    border-radius: 50%;
    background: var(--red);
  }
  .brand-name {
    font-weight: 400;
    font-size: 70px;
    letter-spacing: 2px;
    color: var(--ink);
    text-transform: uppercase;
  }
  .tagline-band {
    position: absolute;
    left: 0; right: 0;
    top: 232px;
    height: 92px;
    background: linear-gradient(90deg, var(--charcoal-dark), var(--charcoal) 60%, var(--charcoal-dark));
    display: flex;
    align-items: center;
    justify-content: center;
    padding: 0 48px;
  }
  .tagline {
    color: var(--white);
    font-size: 15.5px;
    line-height: 1.4;
    text-align: center;
    text-transform: uppercase;
    letter-spacing: 0.3px;
  }

  /* Back side */
  .contact-panel {
    position: absolute;
    top: 0; bottom: 0; left: 0;
    width: 420px;
    background: linear-gradient(160deg, var(--charcoal), var(--charcoal-dark));
    padding: 56px 0 0 62px;
    color: var(--white);
    text-transform: uppercase;
  }
  .person-name {
    font-weight: 900;
    font-size: 26px;
    letter-spacing: 0.5px;
  }
  .person-role {
    font-size: 13px;
    margin-top: 2px;
    letter-spacing: 0.5px;
  }
  .address {
    margin-top: 58px;
    font-size: 14px;
    line-height: 1.35;
    letter-spacing: 0.4px;
  }
  .contact-list {
    list-style: none;
    margin-top: 24px;
    font-size: 15px;
    letter-spacing: 0.4px;
  }
  .contact-list li {
    display: flex;
    align-items: center;
    gap: 10px;
    line-height: 1.5;
  }
  .contact-list svg { width: 16px; height: 16px; flex: none; }
  .mark-circle {
    position: absolute;
    left: 330px;
    top: 102px;
    width: 222px; height: 222px;
    border-radius: 50%;
    background: var(--red);
    border: 7px solid var(--white);
    box-shadow: 0 0 0 1px rgba(0,0,0,0.06);
  }
</style>
</head>
<body>

  <section class="card card-front">
    <div class="brand">
      <span class="brand-dot"></span>
      <span class="brand-name">Brivomar</span>
    </div>
    <div class="tagline-band">
      <p class="tagline">Brivomar is a 3D design services company, providing app, serious/educational game, VR and AR websites/applications to corporate clients.</p>
    </div>
  </section>

  <section class="card card-back">
    <div class="contact-panel">
      <h1 class="person-name">Your Name</h1>
      <p class="person-role">Director</p>
      <p class="address">Unit 12, Harbor Lane<br>Portville</p>
      <ul class="contact-list">
        <li>
          <svg viewBox="0 0 16 16" aria-hidden="true"><path fill="#fff" d="M2 5c0-2 3-3 6-3s6 1 6 3v1h-3V5H5v1H2z M4 7h8l1 7H3z"/></svg>
          5550142876301
        </li>
        <li>
          <svg viewBox="0 0 16 16" aria-hidden="true"><rect x="4" y="1" width="8" height="14" rx="1.5" fill="none" stroke="#fff" stroke-width="1.5"/><circle cx="8" cy="12.5" r="0.9" fill="#fff"/></svg>
          5550198432207
        </li>
        <li>
          <svg viewBox="0 0 16 16" aria-hidden="true"><rect x="1.5" y="3.5" width="13" height="9" fill="none" stroke="#fff" stroke-width="1.4"/><path d="M1.5 3.5 8 9l6.5-5.5" fill="none" stroke="#fff" stroke-width="1.4"/></svg>
          yourmail@mailbox.com
        </li>
        <li>
          <svg viewBox="0 0 16 16" aria-hidden="true"><rect x="1.5" y="2" width="13" height="9" fill="none" stroke="#fff" stroke-width="1.4"/><path d="M6 14h4M8 11v3" stroke="#fff" stroke-width="1.4"/></svg>
          www.yourwesite.com
        </li>
      </ul>
    </div>
    <div class="mark-circle" role="img" aria-label="Brand mark area"></div>
  </section>

</body>
</html>
```